BrightLoft Cleaning Services - inviting website needed to gain residential and commercial clients

Hello! I need a website for a newly created company that specializes in residential and commercial cleaning services. We clean homes, apartments, condos, rental apt for people that are too busy or don't want to spend time cleaning when they can be doing other things - whether that's because of long working hours or a business family schedule or perhaps for seniors that find it challenging to clean their homes.
In addition, for businesses we offer cleaning services of offices, doctors/dentist offices, essentially any business.
The company name is BrightLoft Cleaning Services which means we offer cleaning services not just inside homes and business but also outside. The outside services we offer include lawn mowing, pressure washing and snow removal.
I'm looking for a clean, contemporary design.
We are environmentally continuous and therefore use products that are not harmful to the environment, people or pets.
I should also mention that I would like to offer booking pages on the site as well so that clients can schedule their cleans and pay on line via credit card.
Website copy to be provided shortly but am hoping to see the initial design concept first?? Or if it helps, I can send copy in a few days

```html
<!DOCTYPE html>
<html lang="en">
<head>
<meta charset="utf-8">
<title>BrightLoft Cleaning Services</title>
<link href="https://fonts.googleapis.com/css2?family=Jost:wght@400;500&family=Open+Sans:ital,wght@0,400;0,600;0,700;1,400&display=swap" rel="stylesheet">
<style>
:root{
  --green:#33912f;
  --green-dark:#2c7f29;
  --blue:#1668c9;
  --ink:#222;
  --muted:#666;
  --line:#ddd;
  --white:#fff;
  --band:#4a4a44;
}
*{box-sizing:border-box;margin:0;padding:0}
html,body{width:1200px;height:3136px;overflow:hidden;background:var(--white)}
body{position:relative;font-family:"Open Sans",sans-serif;color:var(--ink)}
.abs{position:absolute}
.heading{font-family:"Jost",sans-serif;font-weight:400}

/* header */
.site-header{position:absolute;left:0;top:0;width:1200px;height:100px;background:var(--white);z-index:3}
.brand{position:absolute;left:91px;top:-24px;width:216px;height:216px;border-radius:50%;background:var(--white);display:flex;align-items:center;justify-content:center;text-align:center;z-index:4}
.brand span{font-family:"Jost",sans-serif;font-weight:500;font-size:26px;line-height:1.15;color:var(--blue);width:150px;margin-top:30px}
.topbar{position:absolute;right:100px;top:15px;font-size:17px;display:flex;align-items:center;gap:12px}
.topbar svg{width:16px;height:16px;fill:var(--green);vertical-align:-2px;margin-right:6px}
.main-nav{position:absolute;right:92px;top:57px;display:flex;gap:36px;font-family:"Jost",sans-serif;font-size:19px;align-items:center}
.main-nav .active{color:var(--green)}
.main-nav svg{width:18px;height:18px}

/* hero */
.hero{position:absolute;left:0;top:100px;width:1200px;height:573px;background:linear-gradient(135deg,#6f5a2c 0%,#b58f3a 30%,#3a3b37 55%,#5a5f58 75%,#2f4a2f 100%)}
.hero h1{position:absolute;left:0;width:1200px;top:140px;text-align:center;font-family:"Jost",sans-serif;font-weight:500;font-size:66px;color:var(--white)}
.hero p{position:absolute;left:0;width:1200px;top:236px;text-align:center;font-size:27px;color:var(--white)}
.btn-solid{position:absolute;left:500px;top:313px;width:200px;height:62px;border-radius:31px;background:var(--green);color:var(--white);font-weight:700;font-size:17px;display:flex;align-items:center;justify-content:center}
.dots{position:absolute;left:563px;top:488px;display:flex;gap:6px}
.dots i{width:13px;height:13px;border-radius:50%;border:2px solid var(--white)}
.dots i:first-child{background:var(--white)}

/* welcome */
.welcome-title{position:absolute;left:0;width:1200px;top:742px;text-align:center;font-size:40px}
.welcome-text{position:absolute;left:224px;width:752px;top:812px;text-align:center;font-size:14px;line-height:26px;color:var(--muted)}
.video{position:absolute;left:380px;top:928px;width:440px;height:274px;border:1px solid var(--line);padding:8px;background:var(--white)}
.video-media{width:100%;height:100%;background:linear-gradient(120deg,#6b6f78,#a9b2bd 50%,#3f6fa6);display:flex;align-items:center;justify-content:center}
.play{width:56px;height:56px;border-radius:50%;background:#111;display:flex;align-items:center;justify-content:center}

/* split */
.split{position:absolute;left:0;top:1305px;width:1200px;height:404px;display:flex}
.split-half{width:600px;height:100%;position:relative;color:var(--white)}
.split-half.res{background:var(--blue)}
.split-half.com{background:var(--green)}
.split-half svg{position:absolute;top:42px}
.split-half h2{position:absolute;top:128px;font-family:"Jost",sans-serif;font-weight:500;font-size:40px}
.split-half p{position:absolute;top:192px;width:420px;font-size:14px;line-height:26px}
.btn-outline{position:absolute;top:298px;width:142px;height:50px;border:2px solid var(--white);border-radius:25px;display:flex;align-items:center;justify-content:center;font-weight:700;font-size:14px}
.split-badge{position:absolute;left:540px;top:1447px;width:120px;height:120px;border-radius:50%;background:var(--white);display:flex;align-items:center;justify-content:center;font-family:"Jost",sans-serif;font-weight:500;font-size:19px;color:var(--blue);z-index:2}

/* services */
.services-title{position:absolute;left:0;width:1200px;top:1790px;text-align:center;font-size:40px}
.service{position:absolute;top:1878px;width:320px;text-align:center}
.service-media{height:240px}
.service-icon{width:84px;height:84px;border-radius:50%;border:4px solid var(--white);margin:-42px auto 0;display:flex;align-items:center;justify-content:center;position:relative}
.service h3{font-family:"Jost",sans-serif;font-weight:500;font-size:27px;margin-top:20px}
.service p{font-size:14px;line-height:26px;color:var(--muted);margin-top:12px}
.service .more{color:var(--green-dark);font-weight:700;font-size:15px;margin-top:18px;display:block}
.arrow{position:absolute;width:40px;height:40px;border-radius:50%;border:1px solid #888;display:flex;align-items:center;justify-content:center}

/* testimonial */
.testimonial{position:absolute;left:0;top:2434px;width:1200px;height:382px;background:linear-gradient(180deg,#45473f,#5d5e55 50%,#3a3b35)}
.testimonial blockquote{position:absolute;left:200px;width:800px;top:163px;text-align:center;font-style:italic;font-size:15px;line-height:28px;color:var(--white)}
.testimonial cite{position:absolute;left:0;width:1200px;top:276px;text-align:center;font-style:normal;font-weight:700;font-size:17px;color:var(--white)}
.testimonial .arrow{border-color:var(--white)}

/* footer */
.social{position:absolute;left:487px;top:2900px;display:flex;gap:10px}
.social i{width:50px;height:50px;border-radius:50%;border:1px solid #999}
.contact-line{position:absolute;left:0;width:1200px;top:2984px;text-align:center;font-size:15px;color:#555}
.contact-line svg{width:14px;height:14px;fill:var(--blue);vertical-align:-2px;margin-right:6px}
.footer-links{position:absolute;left:0;width:1200px;top:3026px;text-align:center;font-size:14px;color:#555}
.copyright{position:absolute;left:0;width:1200px;top:3064px;text-align:center;font-size:14px;color:#555}
.sep{margin:0 12px}
</style>
</head>
<body>

<header class="site-header">
  <div class="brand"><span>BrightLoft Cleaning Services</span></div>
  <div class="topbar">
    <span><svg viewBox="0 0 24 24"><path d="M6.6 10.8a15 15 0 0 0 6.6 6.6l2.2-2.2c.3-.3.7-.4 1-.2 1.1.4 2.3.6 3.6.6.6 0 1 .4 1 1V20c0 .6-.4 1-1 1A17 17 0 0 1 3 4c0-.6.4-1 1-1h3.5c.6 0 1 .4 1 1 0 1.3.2 2.5.6 3.6.1.3 0 .7-.2 1z"/></svg>1 800 555 0142</span>
    <span>|</span>
    <span><svg viewBox="0 0 24 24"><path d="M2 5h20v14H2z M2 5l10 8 10-8" fill="var(--green)"/><path d="M3 6l9 7 9-7" fill="none" stroke="#fff" stroke-width="2"/></svg>hello@brightloftcleaning.com</span>
  </div>
  <nav class="main-nav">
    <span class="active">Home</span><span>About us</span><span>Services</span><span>Blog</span><span>Contact Us</span>
    <svg viewBox="0 0 24 24"><circle cx="10" cy="10" r="6.5" fill="none" stroke="#222" stroke-width="3"/><path d="M15 15l6 6" stroke="#222" stroke-width="3"/></svg>
  </nav>
</header>

<section class="hero" role="img" aria-label="Photo of a gloved hand clearing autumn leaves from a roof gutter">
  <h1>BrightLoft Cleaning Services</h1>
  <p>We Specialises in residential and commercial cleaning services</p>
  <div class="btn-solid">GET MORE INFO</div>
  <div class="dots"><i></i><i></i><i></i><i></i></div>
</section>

<h2 class="welcome-title heading">Welcome to BrightLoft Cleaning Services</h2>
<p class="welcome-text">Nemo enim ipsam voluptatem quia voluptas sit aspernatur aut odit aut fugit, sed quia consequuntur magni dolores eos qui ratione voluptatem sequi nesciunt. Neque porro quisquam est, qui dolorem ipsum quia dolor sit amet, consect etur, adipisci velit, sed quia non numquam eius modi tempora incidunt ut labore et dolore mag</p>
<div class="video">
  <div class="video-media" role="img" aria-label="Video still of a cleaner spraying a window">
    <div class="play"><svg width="22" height="24" viewBox="0 0 22 24"><path d="M4 2l16 10-16 10z" fill="#fff"/></svg></div>
  </div>
</div>

<section class="split">
  <div class="split-half res">
    <svg style="left:98px" width="78" height="64" viewBox="0 0 78 64"><path d="M39 4L2 36h10v26h20V44h14v18h20V36h10z" fill="#fff"/><rect x="56" y="8" width="8" height="16" fill="#fff"/></svg>
    <h2 style="left:97px">Residential</h2>
    <p style="left:100px">Nam libero tempore, cum soluta nobis est eligendi optio cumque nihilm pedit quo minus id quod maxime placeat facere possimus, omnis volupt as assumend omnis dolor repellendus.</p>
    <div class="btn-outline" style="left:100px">READ MORE</div>
  </div>
  <div class="split-half com">
    <svg style="left:90px" width="58" height="72" viewBox="0 0 58 72"><rect x="0" y="0" width="58" height="72" fill="#fff"/><g fill="#33912f"><rect x="8" y="8" width="6" height="5"/><rect x="19" y="8" width="6" height="5"/><rect x="30" y="8" width="6" height="5"/><rect x="41" y="8" width="6" height="5"/><rect x="8" y="19" width="6" height="5"/><rect x="19" y="19" width="6" height="5"/><rect x="30" y="19" width="6" height="5"/><rect x="41" y="19" width="6" height="5"/><rect x="8" y="30" width="6" height="5"/><rect x="19" y="30" width="6" height="5"/><rect x="30" y="30" width="6" height="5"/><rect x="41" y="30" width="6" height="5"/><rect x="8" y="41" width="6" height="5"/><rect x="41" y="41" width="6" height="5"/><rect x="22" y="56" width="14" height="16"/></g></svg>
    <h2 style="left:92px">Commercial</h2>
    <p style="left:92px">Nam libero tempore, cum soluta nobis est eligendi optio cumque nihilm pedit quo minus id quod maxime placeat facere possimus, omnis volupt as assumend omnis dolor repellendus.</p>
    <div class="btn-outline" style="left:92px">READ MORE</div>
  </div>
</section>
<div class="split-badge">BrightLoft</div>

<h2 class="services-title heading">What We Do</h2>
<div class="arrow" style="left:28px;top:1978px"><svg width="12" height="16" viewBox="0 0 12 16"><path d="M9 2L3 8l6 6" fill="none" stroke="#555" stroke-width="2"/></svg></div>
<div class="arrow" style="left:1132px;top:1978px"><svg width="12" height="16" viewBox="0 0 12 16"><path d="M3 2l6 6-6 6" fill="none" stroke="#555" stroke-width="2"/></svg></div>

<article class="service" style="left:98px">
  <div class="service-media" role="img" aria-label="Photo of a lawn mower cutting green grass" style="background:linear-gradient(180deg,#7a8c6a,#5a9a2e 50%,#3f7d1e)"></div>
  <div class="service-icon" style="background:var(--blue)"><svg width="46" height="40" viewBox="0 0 46 40"><path d="M4 4l10 16h24v8H10" fill="none" stroke="#fff" stroke-width="3"/><circle cx="14" cy="32" r="5" fill="#fff"/><circle cx="34" cy="32" r="5" fill="#fff"/></svg></div>
  <h3>Lawn Mowing</h3>
  <p>At vero eos et accusamus et iusto odio digni ssimos ducimus qui blanditiis praesentium volu ptatum deleniti atqu pti quos do</p>
  <span class="more">READ MORE</span>
</article>
<article class="service" style="left:441px">
  <div class="service-media" role="img" aria-label="Photo of a pressure washer cleaning a tiled patio" style="background:linear-gradient(180deg,#4b5a33,#6d6a4a 40%,#9a5a45)"></div>
  <div class="service-icon" style="background:var(--green)"><svg width="40" height="40" viewBox="0 0 40 40"><path d="M14 4C8 14 4 18 4 24a10 10 0 0 0 20 0c0-6-4-10-10-20z" fill="#fff"/><path d="M28 14c-4 7-6 9-6 13a6 6 0 0 0 12 0c0-4-2-6-6-13z" fill="#fff"/></svg></div>
  <h3>Pressure Washing</h3>
  <p>At vero eos et accusamus et iusto odio digni ssimos ducimus qui blanditiis praesentium volu ptatum deleniti atqu pti quos do</p>
  <span class="more">READ MORE</span>
</article>
<article class="service" style="left:782px">
  <div class="service-media" role="img" aria-label="Photo of a snow blower clearing a snowy driveway" style="background:linear-gradient(180deg,#c9d0d6,#e8ecef 55%,#d4d9dd)"></div>
  <div class="service-icon" style="background:var(--blue)"><svg width="30" height="44" viewBox="0 0 30 44"><path d="M9 2h12M15 2v24" stroke="#fff" stroke-width="3"/><path d="M6 26h18v12l-9 4-9-4z" fill="#fff"/></svg></div>
  <h3>Snow Removal</h3>
  <p>At vero eos et accusamus et iusto odio digni ssimos ducimus qui blanditiis praesentium volu ptatum deleniti atqu pti quos do</p>
  <span class="more">READ MORE</span>
</article>

<section class="testimonial" role="img" aria-label="Photo of a pressure washer cleaning a garden path, darkened behind the testimonial">
  <svg class="abs" style="left:567px;top:86px" width="66" height="56" viewBox="0 0 66 56"><path d="M2 56V30C2 14 10 4 26 0l2 6C18 10 14 16 14 24h14v32zM38 56V30C38 14 46 4 62 0l2 6C54 10 50 16 50 24h14v32z" fill="#fff"/></svg>
  <div class="arrow" style="left:99px;top:188px"><svg width="12" height="16" viewBox="0 0 12 16"><path d="M9 2L3 8l6 6" fill="none" stroke="#fff" stroke-width="2"/></svg></div>
  <div class="arrow" style="left:1061px;top:188px"><svg width="12" height="16" viewBox="0 0 12 16"><path d="M3 2l6 6-6 6" fill="none" stroke="#fff" stroke-width="2"/></svg></div>
  <blockquote>“ Nemo enim ipsam voluptatem quia voluptas sit aspernatur aut odit aut fugit, sed quia consequuntur magni dolores eos qui ratione voluptatem sequi nesciunt. Neque porro quisquam est, qui dolorem ipsum quia dolor sit amet, consectetu adipisci velit, sed quia non numquam eius modi tempora incidunt ut labore et dolore mam aliq ”</blockquote>
  <cite>- CLAIRE MORGAN</cite>
</section>

<footer>
  <div class="social"><i></i><i></i><i></i><i></i></div>
  <p class="contact-line">
    <svg viewBox="0 0 24 24"><path d="M12 2a7 7 0 0 0-7 7c0 5 7 13 7 13s7-8 7-13a7 7 0 0 0-7-7zm0 9.5a2.5 2.5 0 1 1 0-5 2.5 2.5 0 0 1 0 5z"/></svg>140 Maple Row, Suite 7, Greenfield<span class="sep">|</span>
    <svg viewBox="0 0 24 24"><path d="M6.6 10.8a15 15 0 0 0 6.6 6.6l2.2-2.2c.3-.3.7-.4 1-.2 1.1.4 2.3.6 3.6.6.6 0 1 .4 1 1V20c0 .6-.4 1-1 1A17 17 0 0 1 3 4c0-.6.4-1 1-1h3.5c.6 0 1 .4 1 1 0 1.3.2 2.5.6 3.6.1.3 0 .7-.2 1z"/></svg>1 800 555 0142<span class="sep">|</span>
    <svg viewBox="0 0 24 24"><path d="M2 5h20v14H2z"/></svg>hello@brightloftcleaning.com
  </p>
  <p class="footer-links">Help<span class="sep">|</span>FAQ<span class="sep">|</span>Support<span class="sep">|</span>Sitemap<span class="sep">|</span>Terms Of Use<span class="sep">|</span>Privacy Statement</p>
  <p class="copyright">Copyrights © 2018, BrightLoft Cleaning Services. All rights reserved.</p>
</footer>

</body>
</html>
```